Stationery/Logo design for law office

Hello, I am looking for a logo and stationery design for my law office. I am a solo practitioner in New York. I would like the logo to be based around my initials: KRW. Original, I know!
Hello:

I need (1) the logo, (2) a letterhead/stationery design, and (3) an envelope design. I would like the logo to be BLUE. Other than that, I am open and looking forward to seeing different designs.

For my privacy, I am using a sample name/information (the real info will be provided to the winning designer). I would like the logo to consist of the KRW design and the words "Marcus R. Welton Law Office." I plan to use a version with both of those elements, as well as just the KRW design alone.

The information that should go in the letterhead and envelope design is the following:

Marcus R. Welton Law Office
742 Alder Lane
Suite 500
New York, New York 10003
212-384-7265
www.weltonlegalfirm.example

I am open to different formats (changing the order of my contact info, writing the phone number without dashes, etc.); I know it's not a ton of content but I would like it to look good -- and I'm open to both classic and more modern looks.

Note that the sample colors I selected are not meant to be exclusive -- there aren't a ton of options.

Thanks in advance!

• I am leaning toward a design just based on my initials, but I am open to ideas -- just nothing trite like scales of justice or a gavel.

```html
<!DOCTYPE html>
<html lang="en">
<head>
<meta charset="utf-8">
<title>Marcus R. Welton Law Office — Stationery</title>
<link rel="stylesheet" href="https://fonts.googleapis.com/css2?family=Open+Sans:wght@400;600;700&display=swap">
<style>
  :root {
    --brand-blue: #2f78b7;
    --brand-blue-bright: #0a96d6;
    --brand-blue-light: #7cc5e8;
    --ink-grey: #666666;
    --ink-dark: #333333;
    --paper: #ffffff;
    --ghost: #f4f4f4;
    --edge: #d9d9d9;
  }
  html, body {
    margin: 0;
    padding: 0;
    width: 1200px;
    height: 1141px;
    overflow: hidden;
    background: var(--paper);
    font-family: "Open Sans", sans-serif;
  }
  .canvas { position: relative; width: 1200px; height: 1141px; }

  /* Letterhead */
  .letterhead {
    position: absolute; left: 174px; top: 0; width: 806px; height: 1141px;
    background: var(--paper); border-left: 1px solid #888; border-right: 1px solid #888;
    box-sizing: border-box; overflow: hidden;
  }
  .letterhead__band { position: absolute; left: 0; top: 0; width: 806px; height: 160px; }
  .letterhead__mark {
    position: absolute; left: 0; width: 100%; top: 68px; text-align: center;
    font-weight: 700; font-size: 40px; color: var(--brand-blue-bright); letter-spacing: 1px; line-height: 1;
  }
  .letterhead__name {
    position: absolute; left: 0; width: 100%; top: 159px; text-align: center;
    font-weight: 600; font-size: 16.5px; color: var(--ink-grey);
  }
  .letterhead__ghost {
    position: absolute; right: 24px; top: 880px;
    font-weight: 700; font-size: 140px; color: var(--ghost); line-height: 1;
  }
  .letterhead__footer {
    position: absolute; left: 0; width: 100%; top: 1093px; text-align: center;
    font-size: 13.5px; color: var(--ink-grey);
  }
  .letterhead__rule {
    position: absolute; left: 0; bottom: 0; width: 100%; height: 13px; background: var(--brand-blue);
  }

  /* Envelope */
  .envelope {
    position: absolute; left: 394px; top: 248px; width: 806px; height: 312px;
    background: var(--paper); border: 1px solid var(--edge); box-sizing: border-box; overflow: hidden;
  }
  .envelope__mark {
    position: absolute; left: 84px; top: 56px; width: 80px; text-align: center;
    font-weight: 700; font-size: 30px; color: var(--brand-blue-bright); line-height: 1;
  }
  .envelope__name {
    position: absolute; left: 40px; top: 110px; font-weight: 600; font-size: 13px; color: var(--ink-grey);
  }
  .envelope__ghost {
    position: absolute; right: 14px; top: 120px;
    font-weight: 700; font-size: 92px; color: var(--ghost); line-height: 1;
  }
  .envelope__band {
    position: absolute; left: 0; bottom: 0; width: 100%; height: 46px; background: var(--brand-blue);
    color: var(--paper); font-size: 13.5px; line-height: 46px; padding-left: 40px; box-sizing: border-box;
  }

  /* Business card, front */
  .card-front {
    position: absolute; left: 0; top: 686px; width: 196px; height: 318px;
    background: var(--paper); border: 1px solid var(--edge); box-sizing: border-box; overflow: hidden;
    text-align: center;
  }
  .card-front__ghost {
    position: absolute; right: -6px; top: 240px;
    font-weight: 700; font-size: 48px; color: #f7f7f7; line-height: 1;
  }
  .card-front__mark {
    position: absolute; left: 0; width: 100%; top: 42px;
    font-weight: 700; font-size: 24px; color: var(--brand-blue-bright); line-height: 1;
  }
  .card-front__name {
    position: absolute; left: 0; width: 100%; top: 91px; font-weight: 700; font-size: 9.5px; color: var(--ink-grey);
  }
  .card-front__divider {
    position: absolute; left: 80px; width: 35px; height: 2px; background: var(--brand-blue-bright);
  }
  .card-front__address {
    position: absolute; left: 0; width: 100%; top: 178px;
    font-size: 10.5px; line-height: 15px; color: var(--ink-dark); margin: 0; font-style: normal;
  }

  /* Business card, back */
  .card-back {
    position: absolute; left: 158px; top: 686px; width: 194px; height: 315px;
    transform-origin: 0 0; transform: rotate(-11deg);
    background: linear-gradient(180deg, var(--brand-blue) 0%, var(--brand-blue-bright) 55%, var(--brand-blue-light) 100%);
    overflow: hidden; text-align: center;
  }
  .card-back__mark {
    position: absolute; left: 0; width: 100%; top: 132px;
    font-weight: 700; font-size: 30px; color: var(--paper); line-height: 1;
  }
  .card-back__name {
    position: absolute; left: 0; width: 100%; top: 184px; font-weight: 600; font-size: 12px; color: var(--paper);
  }
  .card-back__ghost {
    position: absolute; left: 0; width: 100%; top: 262px;
    font-weight: 700; font-size: 64px; color: rgba(255,255,255,0.3); line-height: 1;
  }
</style>
</head>
<body>
<main class="canvas">

  <section class="letterhead" aria-label="Letterhead">
    <svg class="letterhead__band" viewBox="0 0 806 160" aria-hidden="true">
      <path d="M0 0 H806 V160 Q403 70 0 160 Z" fill="#2f78b7"/>
      <rect x="343" y="44" width="120" height="90" rx="30" fill="#ffffff"/>
    </svg>
    <div class="letterhead__mark">KRW</div>
    <div class="letterhead__name">Marcus R. Welton Law Office</div>
    <div class="letterhead__ghost" aria-hidden="true">KRW</div>
    <div class="letterhead__footer">742 Alder Lane, Suite 500, New York, New York 10003, Ph.: 2123847265, www.weltonlegalfirm.example</div>
    <div class="letterhead__rule"></div>
  </section>

  <section class="envelope" aria-label="Envelope">
    <div class="envelope__ghost" aria-hidden="true">KRW</div>
    <div class="envelope__mark">KRW</div>
    <div class="envelope__name">Marcus R. Welton Law Office</div>
    <div class="envelope__band">742 Alder Lane, Suite 500, New York, New York 10003, Ph.: 2123847265, www.weltonlegalfirm.example</div>
  </section>

  <section class="card-front" aria-label="Business card front">
    <div class="card-front__ghost" aria-hidden="true">KRW</div>
    <div class="card-front__mark">KRW</div>
    <div class="card-front__name">Marcus R. Welton Law Office</div>
    <div class="card-front__divider" style="top:154px"></div>
    <address class="card-front__address">
      742 Alder Lane<br>
      Suite 500<br>
      New York, New York 10003<br>
      2123847265<br>
      www.weltonlegalfirm.example
    </address>
    <div class="card-front__divider" style="top:272px"></div>
  </section>

  <section class="card-back" aria-label="Business card back">
    <div class="card-back__mark">KRW</div>
    <div class="card-back__name">Marcus R. Welton Law Office</div>
    <div class="card-back__ghost" aria-hidden="true">KRW</div>
  </section>

</main>
</body>
</html>
```